We are in search of a new business card design for our business. We have a Mexican Grocery Store called Tortilla Grove Market, we would like to see that some have mexican design, but we are open to any type of designs.

Phone: to be announced
Fax: to be announced

Address is:
2415 Calloway Blvd
Larkspur Falls, MD 21407

```html
<!DOCTYPE html>
<html lang="en">
<head>
<meta charset="utf-8">
<title>Tortilla Grove Market – Business Card</title>
<link href="https://fonts.googleapis.com/css2?family=Lato:wght@400;700&display=swap" rel="stylesheet">
<style>
  :root {
    --maroon: #7a2f3b;
    --green: #2e6a45;
    --gold: #c9a13a;
    --card-white: #f4f2ef;
    --text-light: #f3ecec;
    --backdrop: #e9e4dc;
  }
  * { margin: 0; padding: 0; box-sizing: border-box; }
  html, body {
    width: 1200px;
    height: 800px;
    overflow: hidden;
    background: var(--backdrop);
    font-family: "Lato", sans-serif;
  }
  .canvas {
    width: 1200px;
    height: 800px;
    display: flex;
    align-items: center;
    justify-content: center;
  }
  .business-card {
    width: 1000px;
    height: 572px;
    display: block;
    box-shadow: 0 12px 30px rgba(0,0,0,0.18);
  }
  .card-text { font-family: "Lato", sans-serif; fill: var(--text-light); }
  .name-title { font-size: 26px; letter-spacing: 0.3px; }
  .name-title .strong { font-weight: 700; }
  .name-sub { font-size: 20px; }
  .contact-line { font-size: 22px; letter-spacing: 0.6px; }
  .brand-name { font-family: "Lato", sans-serif; font-weight: 700; fill: var(--maroon); }
  .brand-main { font-size: 44px; }
  .brand-sub { font-size: 22px; letter-spacing: 8px; }
</style>
</head>
<body>
<main class="canvas">
  <svg class="business-card" viewBox="0 0 1000 572" xmlns="http://www.w3.org/2000/svg" aria-label="Tortilla Grove Market business card">
    <rect class="card-base" x="0" y="0" width="1000" height="572" fill="var(--maroon)"/>

    <path class="gold-edge" d="M362 0 L474 300 Q500 378 580 381 L1000 384 L1000 397 L575 394 Q488 390 461 305 L349 0 Z" fill="var(--gold)"/>
    <path class="logo-panel" d="M375 0 L1000 0 L1000 384 L580 381 Q500 378 474 300 Z" fill="var(--card-white)"/>

    <path class="name-tab" d="M0 122 L470 122 Q482 122 486 132 L505 256 Q506 266 496 266 L0 266 Z" fill="var(--green)"/>
    <rect class="name-bar" x="68" y="158" width="5" height="70" fill="var(--text-light)"/>
    <text class="card-text name-title" x="98" y="188"><tspan class="strong">TORTILLA GROVE</tspan> MARKET</text>
    <text class="card-text name-sub" x="98" y="220">Suministrar Nombres</text>

    <path class="icon-tab phone-tab" d="M0 315 L112 315 L125 380 L0 380 Z" fill="var(--green)"/>
    <line x1="0" y1="347" x2="52" y2="347" stroke="var(--text-light)" stroke-width="3"/>
    <g class="phone-icon" fill="var(--text-light)" transform="translate(70 337)">
      <path d="M2 6 Q12 -1 22 6 L20 10 L15 8 L15 5 Q12 3.5 9 5 L9 8 L4 10 Z"/>
      <rect x="5" y="11" width="14" height="9" rx="2"/>
    </g>
    <text class="card-text contact-line" x="140" y="341">000 . 1234 . 5678</text>
    <text class="card-text contact-line" x="140" y="370">000 . 9876 . 5432</text>

    <path class="icon-tab web-tab" d="M0 423 L112 423 L125 486 L0 486 Z" fill="var(--green)"/>
    <line x1="0" y1="454" x2="52" y2="454" stroke="var(--text-light)" stroke-width="3"/>
    <g class="globe-icon" fill="none" stroke="var(--text-light)" stroke-width="2" transform="translate(82 454)">
      <circle r="11"/>
      <ellipse rx="5" ry="11"/>
      <line x1="-11" y1="0" x2="11" y2="0"/>
      <line x1="-9" y1="-6" x2="9" y2="-6"/>
      <line x1="-9" y1="6" x2="9" y2="6"/>
    </g>
    <text class="card-text contact-line" x="140" y="450">por suministrar@email.com</text>
    <text class="card-text contact-line" x="140" y="479">www.por suministrar.com</text>

    <path class="icon-tab pin-tab" d="M874 451 L1000 451 L1000 517 L888 517 Z" fill="var(--green)"/>
    <line x1="945" y1="484" x2="1000" y2="484" stroke="var(--text-light)" stroke-width="3"/>
    <g class="pin-icon" transform="translate(917 484)">
      <path d="M0 12 Q-10 0 -10 -5 A10 10 0 0 1 10 -5 Q10 0 0 12 Z" fill="var(--text-light)"/>
      <circle cx="0" cy="-5" r="4" fill="var(--green)"/>
    </g>
    <text class="card-text contact-line" x="850" y="467" text-anchor="end">2415 Calloway Blvd</text>
    <text class="card-text contact-line" x="850" y="496" text-anchor="end">Larkspur Falls, MD 21407</text>

    <g class="brand-lockup">
      <circle cx="760" cy="120" r="18" fill="var(--maroon)"/>
      <text class="brand-name brand-main" x="752" y="210" text-anchor="middle">Tortilla Grove</text>
      <text class="brand-name brand-sub" x="756" y="252" text-anchor="middle">MARKET</text>
    </g>
  </svg>
</main>
</body>
</html>
```